Mirvanto general construction

We need an website that are similar to these websites:
https://www.dulcemor.com/en/
https://pomvilo.com/company/

but with a tweak. Do not copy the entire website but atleast similar and yet better than them.

For reference this our current website.
https://mirvanto.ph/

For the winning Designer please help us with the migration from our old website to the new redesign website.

```html
<!DOCTYPE html>
<html lang="en">
<head>
<meta charset="utf-8">
<title>Mirvanto General Construction — Responsive Website Board</title>
<link href="https://fonts.googleapis.com/css2?family=Oswald:wght@500;600&family=Montserrat:wght@400;600;700;800&display=swap" rel="stylesheet">
<style>
:root{
  --navy:#1b2a4e;
  --navy-dark:#152240;
  --orange:#f26b1d;
  --light:#f2f3f7;
  --ink:#1f2433;
  --muted:#7a8092;
  --white:#ffffff;
  --photo-sky:linear-gradient(180deg,#3f5f8f 0%,#8f7a7a 55%,#d9833a 100%);
  --photo-plant:linear-gradient(180deg,#5b86c2 0%,#9fb6cf 50%,#4a5a6a 100%);
  --photo-blue:linear-gradient(160deg,#2b5fa6,#8fc3e8 60%,#d7e6f2);
  --photo-green:linear-gradient(160deg,#4e6b3a,#8fa67a 60%,#c7cdb7);
  --photo-dusk:linear-gradient(180deg,#5d6f8c,#b08a6a 70%,#7b5a3f);
}
*{box-sizing:border-box;margin:0;padding:0}
html,body{width:1200px;height:1200px;overflow:hidden;background:#fff}
body{font-family:'Montserrat',Arial,sans-serif;color:var(--ink)}
.board{position:absolute;left:0;top:0;width:1920px;height:1920px;transform:scale(.625);transform-origin:0 0;background:#fff}
.device{position:absolute;display:flex;align-items:center;gap:28px}
.device-label{font-family:'Oswald',Impact,sans-serif;font-weight:600;font-size:44px;line-height:1;color:var(--navy-dark);white-space:nowrap}
.page{position:absolute;background:#fff;overflow:hidden}
.ph{background:var(--photo-plant)}
.ph.sky{background:var(--photo-sky)}
.ph.blue{background:var(--photo-blue)}
.ph.green{background:var(--photo-green)}
.ph.dusk{background:var(--photo-dusk)}
.sec{position:relative;overflow:hidden}
.light{background:var(--light)}
.navy{background:var(--navy);color:#fff}
.eyebrow{color:var(--orange);font-size:3px;font-weight:700;text-transform:uppercase;letter-spacing:.2px}
.h2{font-weight:800;text-transform:uppercase;color:var(--navy);line-height:1.05}
.small{font-size:3px;line-height:1.5;color:var(--muted)}
.btn{display:inline-block;background:var(--orange);color:#fff;font-weight:700;text-transform:uppercase;border-radius:1px}
.brand{font-weight:800;color:var(--orange);display:flex;align-items:center;gap:2px}
.brand .dot{background:var(--orange);border-radius:50%}
.badge{border-radius:50%;background:#e9ecf1;border:2px solid #fff}
.icon{background:var(--orange);border-radius:1px;display:inline-block}
.center{text-align:center}
/* desktop */
.d-top{height:36px;position:relative}
.d-top .bar{position:absolute;right:0;top:0;width:340px;height:17px;background:var(--navy);clip-path:polygon(20px 0,100% 0,100% 100%,0 100%);display:flex;justify-content:flex-end;align-items:center;gap:6px;padding-right:18px;font-size:3.2px;color:#fff}
.d-top .bar .btn{font-size:3px;padding:2px 4px}
.d-top nav{position:absolute;right:16px;top:22px;display:flex;gap:7px;font-size:3.6px;font-weight:700;color:var(--navy)}
.d-top .brand{position:absolute;left:10px;top:8px;font-size:5px}
.d-top .brand .dot{width:8px;height:8px}
.d-hero{height:203px;position:relative}
.d-hero .copy{position:absolute;left:18px;top:44px;width:170px;color:#fff}
.d-hero h1{font-size:16px;font-weight:800;line-height:1.05;text-transform:uppercase}
.d-hero p{font-size:3.4px;line-height:1.5;margin-top:5px}
.d-hero .ctas{margin-top:8px;display:flex;gap:8px;align-items:center;font-size:3px}
.d-hero .btn{padding:4px 10px}
.d-hero .badges{position:absolute;left:244px;top:168px;display:flex;gap:8px}
.d-hero .badge{width:36px;height:36px}
.d-about{height:194px;padding:40px 17px 0}
.stat{text-align:center;font-size:2.8px;color:var(--muted)}
.stat b{display:block;font-size:10px;color:var(--navy);font-weight:600}
.grid5{display:grid;grid-template-columns:repeat(5,71px);gap:7px;justify-content:center}
.ind > div{height:97px}
.ind .ph{height:47px}
.ind .t{font-size:3.4px;color:var(--navy);margin-top:14px;text-align:center;text-transform:uppercase}
.ind .s{font-size:2.8px;color:var(--muted);text-align:center;margin-top:3px;line-height:1.5}
.list-item{display:flex;gap:6px;margin-bottom:9px}
.list-item .icon{width:9px;height:9px;flex:none}
.list-item b{display:block;font-size:3.8px;font-weight:600;color:var(--navy)}
.list-item span{font-size:2.8px;color:var(--muted)}
.proj .ph{height:60px}
.proj b{display:block;font-size:3.6px;font-weight:600;margin-top:6px;color:var(--ink)}
.proj span{font-size:3px;color:var(--muted)}
.field{background:#fff;border:1px solid #ccd;height:9px;margin-top:2px;font-size:2.6px;color:#aab;padding:2px}
.f-col h4{color:var(--orange);font-size:3px;margin-bottom:4px}
.f-col li{list-style:none;font-size:3px;color:#dfe3ee;margin-bottom:3px}
.f-col li::before{content:"";display:inline-block;width:2px;height:2px;background:var(--orange);border-radius:50%;margin-right:2px;vertical-align:middle}
/* tablet list */
.t-list{display:grid;grid-template-columns:1fr 1fr;gap:6px 6px}
.t-item{display:flex;gap:3px}
.t-item .icon{width:5px;height:5px;flex:none}
.t-item b{display:block;font-size:2.2px;font-weight:600;color:var(--navy)}
.t-item span{font-size:1.7px;color:var(--muted)}
/* mobile */
.m-sec{padding:4px 3px;overflow:hidden}
.m-h{font-size:2px;font-weight:800;text-transform:uppercase;color:var(--navy);text-align:center;line-height:1.1}
.m-eye{font-size:1.4px;color:var(--orange);text-align:center;font-weight:700;margin-bottom:1px}
.m-card{margin-bottom:7px}
.m-card .ph{height:45px}
.m-card .cap{font-size:1.5px;color:var(--navy);text-align:center;margin-top:4px;text-transform:uppercase}
.m-card .sub{font-size:1.3px;color:var(--muted);text-align:center;margin-top:1px}
.m-card.proj .cap{text-align:left;text-transform:none}
.m-card.proj .sub{text-align:left}
.m-item{text-align:center;margin-bottom:8px}
.m-item .icon{width:3.5px;height:3.5px;display:block;margin:0 auto 1.5px}
.m-item b{display:block;font-size:1.5px;font-weight:600;color:var(--navy)}
.m-item span{font-size:1.2px;color:var(--muted)}
.m-field{background:#fff;border:.5px solid #ccd;height:4px;margin-top:1px}
.m-lbl{font-size:1.2px;color:var(--ink);margin-top:2.5px}
</style>
</head>
<body>
<div class="board">

  <div class="device" style="left:385px;top:110px">
    <span class="device-label">Desktop</span>
    <svg width="116" height="96" viewBox="0 0 116 96"><rect x="3" y="3" width="110" height="72" rx="4" fill="none" stroke="#111" stroke-width="5"/><rect x="50" y="75" width="16" height="12" fill="#111"/><rect x="35" y="86" width="46" height="6" rx="2" fill="#111"/></svg>
  </div>
  <div class="device" style="left:996px;top:115px">
    <span class="device-label">Tablet</span>
    <svg width="66" height="90" viewBox="0 0 66 90"><rect x="3" y="3" width="60" height="84" rx="6" fill="none" stroke="#111" stroke-width="5"/><circle cx="33" cy="78" r="4" fill="#111"/></svg>
  </div>
  <div class="device" style="left:1465px;top:95px">
    <span class="device-label">Mobile</span>
    <svg width="58" height="104" viewBox="0 0 58 104"><rect x="3" y="3" width="52" height="98" rx="7" fill="none" stroke="#111" stroke-width="5"/><rect x="20" y="10" width="18" height="4" rx="2" fill="#111"/><circle cx="29" cy="88" r="5" fill="#111"/></svg>
  </div>

  <!-- DESKTOP PAGE -->
  <div class="page" style="left:299px;top:222px;width:416px;height:1655px">
    <header class="d-top">
      <div class="brand"><span class="dot"></span>MIRVANTO</div>
      <div class="bar"><span>info@mirvanto.ph</span><span>+63 (0) 45 210-3377</span><span>+63 (0) 917-550-2816</span><span class="btn">Request a Quote</span></div>
      <nav><span>HOME</span><span>ABOUT US</span><span>INDUSTRIES</span><span>SERVICES</span><span>PROJECTS</span><span>SUSTAINABILITY</span><span>CAREERS</span><span>NEWS</span><span>CONTACT</span></nav>
    </header>
    <section class="d-hero ph sky" role="img" aria-label="Industrial refinery at sunset">
      <div class="copy">
        <h1>One Step Ahead in Industrial Construction</h1>
        <p>Building the infrastructure that powers industries. Mirvanto delivers world-class engineering, construction, maintenance and industrial support services across Oil &amp; Gas, Power Generation, Water Treatment, Environmental Management, and infrastructure projects.</p>
        <div class="ctas"><span class="btn">Start Your Project →</span><span>▮ View Our Projects →</span></div>
      </div>
      <div class="badges"><div class="badge"></div><div class="badge"></div><div class="badge"></div></div>
    </section>
    <section class="sec light d-about" style="display:flex;gap:8px">
      <div class="ph blue" role="img" aria-label="Industrial plant at dusk" style="width:188px;height:125px;border-radius:2px"></div>
      <div style="flex:1;margin-top:-8px">
        <div class="eyebrow">About Mirvanto</div>
        <div class="h2" style="font-size:7.5px;margin:4px 0">Building Strong Foundations Since Day One</div>
        <p class="small">With more than four years of established business relationships with various blue chip clients and major construction companies, we at Mirvanto can provide a wide range of services to the oil, gas, energy, and environmental sectors. While we aim for sustainability and profitability in all our projects, we strive to protect the environment and the health and safety of our people and the communities where we operate.</p>
        <div style="text-align:right;margin-top:5px"><span class="btn" style="font-size:3px;padding:2px 6px">Know More About Us</span></div>
        <div style="display:flex;justify-content:space-around;margin-top:10px">
          <div class="stat"><span class="icon" style="width:9px;height:9px"></span><b>20+</b>Years Experience</div>
          <div class="stat"><span class="icon" style="width:9px;height:9px"></span><b>98%</b>Client Satisfaction</div>
          <div class="stat"><span class="icon" style="width:9px;height:9px"></span><b>1,000+</b>Qualified Workforce</div>
        </div>
      </div>
    </section>
    <section class="sec" style="height:260px;padding-top:18px">
      <div class="eyebrow center">Industries</div>
      <div class="h2 center" style="font-size:8px;margin:5px 0 8px;font-weight:700">Industries We Serve</div>
      <div class="grid5 ind">
        <div><div class="ph" role="img" aria-label="Oil and gas tank farm"></div><div class="t">Oil &amp; Gas</div><div class="s">Offshore &amp; Onshore Industrial Services</div></div>
        <div><div class="ph dusk" role="img" aria-label="Power station"></div><div class="t">Power Generation</div><div class="s">Maintenance • Shutdown • EPC</div></div>
        <div><div class="ph blue" role="img" aria-label="Water treatment pipes"></div><div class="t">Water Treatment</div><div class="s">Desalination &amp; Treatment Plants</div></div>
        <div><div class="ph green" role="img" aria-label="Environmental facility"></div><div class="t">Environmental Solutions</div><div class="s">Waste-to-Energy &amp; Sustainable Infrastructure</div></div>
        <div><div class="ph sky" role="img" aria-label="Construction crane"></div><div class="t">General Construction</div><div class="s">Industrial Buildings &amp; Civil Engineering</div></div>
        <div><div class="ph" role="img" aria-label="Oil and gas tank farm"></div><div class="t">Oil &amp; Gas</div><div class="s">Offshore &amp; Onshore Industrial Services</div></div>
        <div><div class="ph dusk" role="img" aria-label="Power station"></div><div class="t">Power Generation</div><div class="s">Maintenance • Shutdown • EPC</div></div>
        <div><div class="ph blue" role="img" aria-label="Water treatment pipes"></div><div class="t">Water Treatment</div><div class="s">Desalination &amp; Treatment Plants</div></div>
        <div><div class="ph green" role="img" aria-label="Environmental facility"></div><div class="t">Environmental Solutions</div><div class="s">Waste-to-Energy &amp; Sustainable Infrastructure</div></div>
        <div><div class="ph sky" role="img" aria-label="Construction crane"></div><div class="t">General Construction</div><div class="s">Industrial Buildings &amp; Civil Engineering</div></div>
      </div>
    </section>
    <section class="sec light" style="height:210px;padding:20px 17px 0;display:flex;gap:8px">
      <div class="ph dusk" role="img" aria-label="Two workers in orange coveralls at a refinery" style="width:188px;height:125px;margin-top:22px;border-radius:2px"></div>
      <div style="flex:1">
        <div class="eyebrow">Why Choose Us</div>
        <div class="h2" style="font-size:7px;margin:4px 0 8px;font-weight:700">Why Industry Leaders Choose Mirvanto</div>
        <div class="list-item"><span class="icon"></span><div><b>Safety Excellence</b><span>Zero-compromise safety culture.</span></div></div>
        <div class="list-item"><span class="icon"></span><div><b>Skilled Workforce</b><span>Certified engineers and specialists.</span></div></div>
        <div class="list-item"><span class="icon"></span><div><b>End-To-End Solutions</b><span>Engineering to maintenance under one partner.</span></div></div>
        <div class="list-item"><span class="icon"></span><div><b>On-Time Delivery</b><span>Reliable scheduling and execution.</span></div></div>
        <div class="list-item"><span class="icon"></span><div><b>Sustainable Practices</b><span>Environmentally responsible operations.</span></div></div>
        <div class="list-item"><span class="icon"></span><div><b>Global Standards</b><span>International quality management systems.</span></div></div>
      </div>
    </section>
    <section class="sec" style="height:163px;padding:20px 17px 0;display:flex;gap:12px">
      <div style="flex:1">
        <div class="eyebrow">What We Do</div>
        <div class="h2" style="font-size:7px;margin:4px 0 8px;font-weight:700">Comprehensive Solutions Across the Project Lifecycle</div>
        <div style="display:grid;grid-template-columns:1fr 1fr;gap:0 8px">
          <div class="list-item"><span class="icon"></span><div><b>Engineering &amp; Construction</b><span>Industrial civil and mechanical works.</span></div></div>
          <div class="list-item"><span class="icon"></span><div><b>Plant Maintenance</b><span>Preventive and corrective maintenance.</span></div></div>
          <div class="list-item"><span class="icon"></span><div><b>Shutdown &amp; Turnaround</b><span>Fast execution with minimal downtime.</span></div></div>
          <div class="list-item"><span class="icon"></span><div><b>Scaffolding &amp; Rope Access</b><span>Safe access for complex structures.</span></div></div>
          <div class="list-item"><span class="icon"></span><div><b>Mechanical &amp; Electrical Installation</b><span>Industrial-grade installation services.</span></div></div>
          <div class="list-item"><span class="icon"></span><div><b>Environmental Engineering</b><span>Waste treatment and remediation solutions.</span></div></div>
        </div>
        <span class="btn" style="font-size:3px;padding:2px 6px">View All Services →</span>
      </div>
      <div style="width:147px;display:grid;grid-template-columns:84px 61px;grid-template-rows:48px 48px;gap:2px">
        <div class="ph blue" role="img" aria-label="Aerial view of refinery" style="grid-row:span 2"></div>
        <div class="ph" role="img" aria-label="Refinery towers"></div>
        <div class="ph sky" role="img" aria-label="Oil pump at sunset"></div>
      </div>
    </section>
    <section class="sec light" style="height:147px;padding:16px 17px 0">
      <div class="eyebrow center">Portfolio</div>
      <div class="h2 center" style="font-size:8px;margin:5px 0 8px;font-weight:700">Featured Projects</div>
      <div style="display:grid;grid-template-columns:repeat(4,1fr);gap:6px">
        <div class="proj"><div class="ph" role="img" aria-label="Refinery"></div><b>Refinery Upgrading Project</b><span>Oil &amp; Gas</span></div>
        <div class="proj"><div class="ph sky" role="img" aria-label="Power plant"></div><b>Power Plant Maintenance</b><span>Power Generation</span></div>
        <div class="proj"><div class="ph blue" role="img" aria-label="Desalination pipes"></div><b>Desalination Plant Project</b><span>Water Treatment</span></div>
        <div class="proj"><div class="ph green" role="img" aria-label="Waste-to-energy facility"></div><b>Waste-To-Energy Facility</b><span>Environmental Solutions</span></div>
      </div>
    </section>
    <section class="sec navy center" style="height:90px;padding-top:18px">
      <div style="font-size:13px;font-weight:800">READY TO BUILD THE FUTURE TOGETHER?</div>
      <div style="font-size:3.6px;margin-top:4px">Whether you're planning a new industrial facility or maintaining critical infrastructure, our team is ready to deliver world-class solutions.</div>
      <div style="margin-top:14px;font-size:3px;display:flex;justify-content:center;gap:20px;align-items:center"><span class="btn" style="padding:4px 20px">Start Your Project →</span><span>▮ Contact Our Team →</span></div>
    </section>
    <section class="sec center" style="height:82px;padding-top:18px">
      <div class="eyebrow">How We Work</div>
      <div class="h2" style="font-size:8px;margin:4px 0 12px;font-weight:700">Our Process</div>
      <div style="display:flex;justify-content:center;gap:28px;font-size:3.2px;color:var(--muted)">
        <span>❶ ▪ Consultation</span><span>❷ ▪ Engineering</span><span>❸ ▪ Planning</span><span>❹ ▪ Construction</span><span>❺ ▪ Testing</span><span>❻ ▪ Maintenance</span>
      </div>
    </section>
    <section class="sec" style="height:134px;display:flex">
      <div class="navy" style="width:205px;position:relative;padding:14px 14px">
        <div class="ph dusk" role="img" aria-label="Engineers reviewing plans on site" style="position:absolute;right:0;top:0;width:110px;height:100%;clip-path:polygon(30% 0,100% 0,100% 100%,0 100%)"></div>
        <div style="position:relative;width:100px">
          <div style="font-size:7px;font-weight:700">SAFETY &amp; QUALITY</div>
          <div style="font-size:3px;margin-top:4px;line-height:1.5">Safety is our highest priority.<br><br>We maintain internationally recognized quality, environmental, and occupational safety standards.</div>
          <div style="font-size:7px;margin-top:6px">Certifications</div>
          <div style="font-size:3px;line-height:1.6;margin-top:2px">• ISO Certified<br>• PCAB Licensed<br>• HSE Compliant<br>• QA/QC Assured</div>
          <span class="btn" style="font-size:3px;padding:2px 6px;margin-top:4px">Learn More →</span>
        </div>
      </div>
      <div class="light" style="flex:1;padding:10px 13px">
        <div style="font-size:7px;font-weight:700;color:var(--navy)">GET IN TOUCH</div>
        <div class="small" style="margin:3px 0 6px">Don't hesitate to reach out today. We'll be in touch shortly to start discussing your project goals.</div>
        <div style="display:grid;grid-template-columns:1fr 1fr;gap:3px 8px;font-size:2.8px">
          <div>Name<div class="field">Name</div></div><div>Subject<div class="field">Subject</div></div>
          <div>Email<div class="field">Email</div></div><div>Phone<div class="field">Phone</div></div>
        </div>
        <div style="font-size:2.8px;margin-top:3px">Message<div class="field" style="height:24px">Message</div></div>
        <div class="btn center" style="display:block;font-size:3px;padding:2px;margin-top:4px">Submit ➔</div>
      </div>
    </section>
    <footer class="sec" style="height:136px;background:var(--navy-dark);color:#fff;padding:20px 16px 0">
      <div style="display:flex;gap:14px">
        <div style="width:78px">
          <div class="brand" style="font-size:5px;justify-content:center"><span class="dot" style="width:9px;height:9px"></span>MIRVANTO</div>
          <div style="font-size:3.2px;line-height:1.5;margin-top:10px">Mirvanto General Construction delivers world-class industrial construction, maintenance, engineering solutions with safety, quality, and integrity at the core of everything we do.</div>
        </div>
        <ul class="f-col" style="width:50px"><h4>QUICK LINKS</h4><li>About Us</li><li>Projects</li><li>Industries</li><li>Sustainability</li><li>Careers</li><li>News</li><li>Contact Us</li></ul>
        <ul class="f-col" style="width:66px"><h4>INDUSTRIES</h4><li>Oil &amp; Gas</li><li>Power Generation</li><li>Water Treatment</li><li>Environmental Solutions</li><li>General Construction</li></ul>
        <ul class="f-col" style="width:66px"><h4>SERVICES</h4><li>Engineering &amp; Construction</li><li>Plant Maintenance</li><li>Shutdown &amp; Turnaround</li><li>Scaffolding &amp; Rope Access</li><li>Mechanical &amp; Electrical</li><li>Environmental Engineering</li></ul>
        <ul class="f-col" style="width:70px"><h4>GET IN TOUCH</h4><li>14 Kalayaan Ridge Rd. Brgy. Malinta, Tanauan City, Batangas</li><li>+63 (0) 45 210-3377</li><li>+63 (0) 917-550-2816</li><li>info@mirvanto.ph</li></ul>
      </div>
      <div class="center" style="font-size:3px;margin-top:16px">Copyright © 2026 MIRVANTO | Powered By MIRVANTO</div>
    </footer>
  </div>

  <!-- TABLET PAGE -->
  <div class="page" style="left:988px;top:222px;width:171px;height:1690px">
    <div style="height:8px;background:var(--navy);font-size:2px;color:#fff;display:flex;gap:4px;align-items:center;padding:0 3px">info@mirvanto.ph · +63 (0) 45 210-3377 · +63 (0) 917-550-2816 <span class="btn" style="padding:1px 2px;margin-left:auto">Request a Quote</span></div>
    <div style="height:24px;display:flex;align-items:center;justify-content:space-between;padding:0 6px"><div class="brand" style="font-size:3px"><span class="dot" style="width:5px;height:5px"></span>MIRVANTO</div><span style="width:10px;height:10px;border-radius:50%;background:var(--orange)"></span></div>
    <div class="ph sky" role="img" aria-label="Industrial refinery at sunset" style="height:114px;padding:24px 9px;color:#fff;position:relative">
      <div style="font-size:6px;font-weight:800;line-height:1.05">ONE STEP AHEAD IN INDUSTRIAL CONSTRUCTION</div>
      <div style="font-size:2.2px;margin-top:3px;line-height:1.5">Building the infrastructure that powers industries. Mirvanto delivers world-class engineering, construction, maintenance and industrial support services across Oil &amp; Gas, Power, Water, Environmental and infrastructure projects.</div>
      <div style="font-size:2px;margin-top:5px"><span class="btn" style="padding:2px 8px">Start Your Project →</span> &nbsp; View Our Projects →</div>
      <div style="position:absolute;left:85px;bottom:8px;display:flex;gap:5px"><div class="badge" style="width:18px;height:18px"></div><div class="badge" style="width:18px;height:18px"></div><div class="badge" style="width:18px;height:18px"></div></div>
    </div>
    <div class="light" style="height:239px;padding:16px 8px">
      <div class="eyebrow center" style="font-size:2px">About Mirvanto</div>
      <div class="h2 center" style="font-size:5px;font-weight:700;margin:2px 0 5px">Building Strong Foundations Since Day One</div>
      <div class="ph blue" role="img" aria-label="Industrial plant at dusk" style="height:104px"></div>
      <div class="small" style="font-size:2px;margin-top:5px">With more than four years of established business relationships with various blue chip clients and major construction companies, we provide a wide range of services to the oil, gas, energy and environmental sectors.</div>
      <div style="text-align:right;margin-top:5px"><span class="btn" style="font-size:2px;padding:1px 4px">Know More About Us</span></div>
      <div style="display:flex;justify-content:space-around;margin-top:4px;font-size:1.8px" class="stat">
        <div><span class="icon" style="width:5px;height:5px"></span><b style="font-size:4px">20+</b>Years Experience</div>
        <div><span class="icon" style="width:5px;height:5px"></span><b style="font-size:4px">98%</b>Client Satisfaction</div>
        <div><span class="icon" style="width:5px;height:5px"></span><b style="font-size:4px">1,000+</b>Qualified Workforce</div>
      </div>
    </div>
    <div style="height:273px;padding:8px 8px">
      <div class="eyebrow center" style="font-size:2px">Industries</div>
      <div class="h2 center" style="font-size:4.5px;font-weight:700;margin:2px 0 5px">Industries We Serve</div>
      <div style="display:grid;grid-template-columns:1fr 1fr;gap:4px 5px;font-size:2px;text-align:center;color:var(--navy)">
        <div><div class="ph" role="img" aria-label="Oil and gas" style="height:50px"></div><div style="margin-top:6px">OIL &amp; GAS</div><div style="font-size:1.6px;color:var(--muted);margin-top:2px">Offshore &amp; Onshore Industrial Services</div></div>
        <div><div class="ph dusk" role="img" aria-label="Power station" style="height:50px"></div><div style="margin-top:6px">POWER GENERATION</div><div style="font-size:1.6px;color:var(--muted);margin-top:2px">Maintenance • Shutdown • EPC</div></div>
        <div><div class="ph blue" role="img" aria-label="Water treatment" style="height:50px"></div><div style="margin-top:6px">WATER TREATMENT</div><div style="font-size:1.6px;color:var(--muted);margin-top:2px">Desalination &amp; Treatment Plants</div></div>
        <div><div class="ph green" role="img" aria-label="Environmental facility" style="height:50px"></div><div style="margin-top:6px">ENVIRONMENTAL SOLUTIONS</div><div style="font-size:1.6px;color:var(--muted);margin-top:2px">Waste-to-Energy &amp; Sustainable Infrastructure</div></div>
        <div><div class="ph sky" role="img" aria-label="Construction crane" style="height:50px"></div><div style="margin-top:6px">GENERAL CONSTRUCTION</div><div style="font-size:1.6px;color:var(--muted);margin-top:2px">Industrial Buildings &amp; Civil Engineering</div></div>
        <div class="navy" style="height:76px;padding:6px 4px;border-radius:1px"><div style="font-size:4px;font-weight:600">Ready to Start Your Next Project?</div><div style="font-size:1.8px;margin:3px 0">Whether you're planning a new industrial facility, our team is ready to deliver.</div><span class="btn" style="padding:1px 4px">Contact Us Now</span></div>
      </div>
    </div>
    <div class="light" style="height:220px;padding:8px 8px">
      <div class="eyebrow center" style="font-size:2px">Why Choose Us</div>
      <div class="h2 center" style="font-size:4.3px;font-weight:700;margin:2px 0 5px">Why Industry Leaders Choose Mirvanto</div>
      <div class="ph dusk" role="img" aria-label="Workers in orange coveralls at refinery" style="height:103px"></div>
      <div class="t-list" style="margin-top:6px">
        <div class="t-item"><span class="icon"></span><div><b>Safety Excellence</b><span>Zero-compromise safety culture.</span></div></div>
        <div class="t-item"><span class="icon"></span><div><b>Skilled Workforce</b><span>Certified engineers and specialists.</span></div></div>
        <div class="t-item"><span class="icon"></span><div><b>End-To-End Solutions</b><span>Engineering to maintenance under one partner.</span></div></div>
        <div class="t-item"><span class="icon"></span><div><b>On-Time Delivery</b><span>Reliable scheduling and execution.</span></div></div>
        <div class="t-item"><span class="icon"></span><div><b>Sustainable Practices</b><span>Environmentally responsible operations.</span></div></div>
        <div class="t-item"><span class="icon"></span><div><b>Global Standards</b><span>International quality management systems.</span></div></div>
      </div>
    </div>
    <div style="height:125px;padding:8px 8px">
      <div class="eyebrow center" style="font-size:2px">What We Do</div>
      <div class="h2 center" style="font-size:4.3px;font-weight:700;margin:2px 0 6px">Comprehensive Solutions Across the Project Lifecycle</div>
      <div class="t-list">
        <div class="t-item"><span class="icon"></span><div><b>Engineering &amp; Construction</b><span>Industrial civil and mechanical works.</span></div></div>
        <div class="t-item"><span class="icon"></span><div><b>Plant Maintenance</b><span>Preventive and corrective maintenance.</span></div></div>
        <div class="t-item"><span class="icon"></span><div><b>Shutdown &amp; Turnaround</b><span>Fast execution with minimal downtime.</span></div></div>
        <div class="t-item"><span class="icon"></span><div><b>Scaffolding &amp; Rope Access</b><span>Safe access for complex structures.</span></div></div>
        <div class="t-item"><span class="icon"></span><div><b>Mechanical &amp; Electrical Installation</b><span>Industrial-grade installation services.</span></div></div>
        <div class="t-item"><span class="icon"></span><div><b>Environmental Engineering</b><span>Waste treatment and remediation solutions.</span></div></div>
      </div>
      <div class="center" style="margin-top:6px"><span class="btn" style="font-size:2px;padding:1px 5px">View All Services</span></div>
    </div>
    <div class="light" style="height:175px;padding:8px 8px">
      <div class="eyebrow center" style="font-size:2px">Portfolio</div>
      <div class="h2 center" style="font-size:4.5px;font-weight:700;margin:2px 0 5px">Featured Projects</div>
      <div style="display:grid;grid-template-columns:1fr 1fr;gap:5px;font-size:2px">
        <div><div class="ph" role="img" aria-label="Refinery" style="height:50px"></div>Refinery Upgrading Project<br><span style="color:var(--muted);font-size:1.7px">Oil &amp; Gas</span></div>
        <div><div class="ph sky" role="img" aria-label="Power plant" style="height:50px"></div>Power Plant Maintenance<br><span style="color:var(--muted);font-size:1.7px">Power Generation</span></div>
        <div><div class="ph blue" role="img" aria-label="Desalination plant" style="height:50px"></div>Desalination Plant Project<br><span style="color:var(--muted);font-size:1.7px">Water Treatment</span></div>
        <div><div class="ph green" role="img" aria-label="Waste-to-energy facility" style="height:50px"></div>Waste-To-Energy Facility<br><span style="color:var(--muted);font-size:1.7px">Environmental Solutions</span></div>
      </div>
    </div>
    <div class="navy center" style="height:58px;padding-top:10px"><div style="font-size:4.5px;font-weight:700">READY TO BUILD THE FUTURE TOGETHER?</div><div style="font-size:1.8px;margin:3px 0 6px">Our team is ready to deliver world-class solutions.</div><span class="btn" style="font-size:2px;padding:2px 8px">Start Your Project →</span></div>
    <div class="center" style="height:75px;padding-top:8px"><div class="eyebrow" style="font-size:2px">How We Work</div><div class="h2" style="font-size:4.5px;font-weight:700">Our Process</div>
      <div style="display:grid;grid-template-columns:repeat(3,1fr);gap:10px;font-size:2px;color:var(--muted);margin-top:8px"><span>❶ Consultation</span><span>❷ Engineering</span><span>❸ Planning</span><span>❹ Construction</span><span>❺ Testing</span><span>❻ Maintenance</span></div></div>
    <div class="navy" style="height:92px;display:flex;padding:8px 6px;position:relative">
      <div style="width:70px;font-size:2px;line-height:1.5;position:relative"><div style="font-size:4px;font-weight:700">SAFETY &amp; QUALITY</div>Safety is our highest priority. We maintain recognized quality and safety standards.<div style="font-size:4px;margin-top:3px">Certifications</div>• ISO Certified<br>• PCAB Licensed<br>• HSE Compliant<br>• QA/QC Assured<br><span class="btn" style="padding:1px 4px;margin-top:2px">Learn More</span></div>
      <div class="ph dusk" role="img" aria-label="Engineers reviewing plans" style="position:absolute;right:0;top:0;width:85px;height:100%"></div>
    </div>
    <div class="light" style="height:106px;padding:8px 6px">
      <div style="font-size:4px;font-weight:700;color:var(--navy)">GET IN TOUCH</div>
      <div style="font-size:1.7px;color:var(--muted);margin-top:2px">Don't hesitate to reach out today. We'll be in touch shortly.</div>
      <div style="display:grid;grid-template-columns:1fr 1fr;gap:3px 6px;margin-top:4px"><div class="field" style="height:5px"></div><div class="field" style="height:5px"></div><div class="field" style="height:5px"></div><div class="field" style="height:5px"></div></div>
      <div class="field" style="height:18px;margin-top:4px"></div>
      <div class="btn center" style="display:block;font-size:2px;margin-top:4px;padding:1px">Submit</div>
    </div>
    <div style="height:181px;background:var(--navy-dark);padding:10px 6px;color:#fff">
      <div class="brand" style="font-size:3px;justify-content:center"><span class="dot" style="width:6px;height:6px"></span>MIRVANTO</div>
      <div class="center" style="font-size:2px;margin:6px 0 10px">Mirvanto General Construction delivers world-class industrial construction, maintenance and engineering solutions.</div>
      <div style="display:grid;grid-template-columns:1fr 1fr;gap:8px">
        <ul class="f-col"><h4 style="font-size:2px">QUICK LINKS</h4><li style="font-size:2px">About Us</li><li style="font-size:2px">Projects</li><li style="font-size:2px">Careers</li><li style="font-size:2px">Contact Us</li></ul>
        <ul class="f-col"><h4 style="font-size:2px">INDUSTRIES</h4><li style="font-size:2px">Oil &amp; Gas</li><li style="font-size:2px">Power Generation</li><li style="font-size:2px">Water Treatment</li></ul>
        <ul class="f-col"><h4 style="font-size:2px">SERVICES</h4><li style="font-size:2px">Plant Maintenance</li><li style="font-size:2px">Shutdown &amp; Turnaround</li><li style="font-size:2px">Scaffolding</li></ul>
        <ul class="f-col"><h4 style="font-size:2px">GET IN TOUCH</h4><li style="font-size:2px">Tanauan City, Batangas</li><li style="font-size:2px">+63 (0) 45 210-3377</li><li style="font-size:2px">info@mirvanto.ph</li></ul>
      </div>
      <div class="center" style="font-size:1.8px;margin-top:10px">Copyright © 2026 MIRVANTO</div>
    </div>
  </div>

  <!-- MOBILE PAGE -->
  <div class="page" style="left:1478px;top:210px;width:71px;height:1705px">
    <div style="height:22px;display:flex;justify-content:space-between;align-items:center;padding:0 4px"><div class="brand" style="font-size:2px"><span class="dot" style="width:4px;height:4px"></span>MIRVANTO</div><span style="width:6px;height:6px;border-radius:50%;background:var(--orange)"></span></div>
    <div class="ph sky" role="img" aria-label="Industrial refinery at sunset" style="height:58px;padding:8px 3px;color:#fff"><div style="font-size:2.6px;font-weight:800;line-height:1.1">ONE STEP AHEAD IN INDUSTRIAL CONSTRUCTION</div><div style="font-size:1.4px;margin-top:2px;line-height:1.5">Building the infrastructure that powers industries. World-class engineering, construction and maintenance services.</div><div style="margin-top:4px;font-size:1.3px"><span class="btn" style="padding:1px 3px">Start Your Project</span> View Projects</div></div>
    <div style="height:25px;display:flex;justify-content:center;gap:3px;align-items:center"><div class="badge" style="width:12px;height:12px"></div><div class="badge" style="width:12px;height:12px"></div><div class="badge" style="width:12px;height:12px"></div></div>
    <div class="light m-sec" style="height:183px">
      <div class="m-eye">ABOUT MIRVANTO</div>
      <div class="m-h">Building Strong Foundations Since Day One</div>
      <div class="ph blue" role="img" aria-label="Industrial plant" style="height:42px;margin-top:3px"></div>
      <div class="small" style="font-size:1.3px;margin-top:3px">With more than four years of established business relationships with blue chip clients and major construction companies, we serve the oil, gas, energy and environmental sectors while protecting our people and communities.</div>
      <div class="center" style="margin-top:3px"><span class="btn" style="font-size:1.2px;padding:1px 3px">Know More About Us</span></div>
      <div class="stat center" style="font-size:1.3px;margin-top:6px">
        <span class="icon" style="width:3.5px;height:3.5px"></span><b style="font-size:2.4px">20+</b>Years Experience
        <div style="height:6px"></div>
        <span class="icon" style="width:3.5px;height:3.5px"></span><b style="font-size:2.4px">98%</b>Client Satisfaction
        <div style="height:6px"></div>
        <span class="icon" style="width:3.5px;height:3.5px"></span><b style="font-size:2.4px">1,000+</b>Qualified Workforce
      </div>
    </div>
    <div class="m-sec" style="height:374px">
      <div class="m-eye">INDUSTRIES</div>
      <div class="m-h" style="margin-bottom:4px">Industries We Serve</div>
      <div class="m-card"><div class="ph" role="img" aria-label="Oil and gas"></div><div class="cap">Oil &amp; Gas</div><div class="sub">Offshore &amp; Onshore Industrial Services</div></div>
      <div class="m-card"><div class="ph dusk" role="img" aria-label="Power station"></div><div class="cap">Power Generation</div><div class="sub">Maintenance • Shutdown • EPC</div></div>
      <div class="m-card"><div class="ph blue" role="img" aria-label="Water treatment"></div><div class="cap">Water Treatment</div><div class="sub">Desalination &amp; Treatment Plants</div></div>
      <div class="m-card"><div class="ph green" role="img" aria-label="Environmental facility"></div><div class="cap">Environmental Solutions</div><div class="sub">Waste-to-Energy &amp; Sustainable Infrastructure</div></div>
      <div class="m-card"><div class="ph sky" role="img" aria-label="Construction crane"></div><div class="cap">General Construction</div><div class="sub">Industrial Buildings &amp; Civil Engineering</div></div>
      <div class="navy center" style="height:30px;padding:3px 2px;font-size:1.6px;font-weight:600">Ready to Start Your Next Project?<div style="font-size:1.2px;font-weight:400;margin:2px 0">Our team is ready to deliver world-class solutions.</div><span class="btn" style="font-size:1.2px;padding:1px 3px">Contact Us Now</span></div>
    </div>
    <div class="light m-sec" style="height:208px">
      <div class="m-eye">WHY CHOOSE US</div>
      <div class="m-h">Why Industry Leaders Choose Mirvanto</div>
      <div class="ph dusk" role="img" aria-label="Workers at refinery" style="height:42px;margin:3px 0 8px"></div>
      <div class="m-item"><span class="icon"></span><b>Safety Excellence</b><span>Zero-compromise safety culture.</span></div>
      <div class="m-item"><span class="icon"></span><b>Skilled Workforce</b><span>Certified engineers and specialists.</span></div>
      <div class="m-item"><span class="icon"></span><b>End-To-End Solutions</b><span>Engineering to maintenance under one partner.</span></div>
      <div class="m-item"><span class="icon"></span><b>On-Time Delivery</b><span>Reliable scheduling and execution.</span></div>
      <div class="m-item"><span class="icon"></span><b>Sustainable Practices</b><span>Environmentally responsible operations.</span></div>
      <div class="m-item"><span class="icon"></span><b>Global Standards</b><span>International quality management systems.</span></div>
    </div>
    <div class="m-sec" style="height:166px">
      <div class="m-eye">WHAT WE DO</div>
      <div class="m-h" style="margin-bottom:6px">Comprehensive Solutions Across the Project Lifecycle</div>
      <div class="m-item"><span class="icon"></span><b>Engineering &amp; Construction</b><span>Industrial civil and mechanical works.</span></div>
      <div class="m-item"><span class="icon"></span><b>Shutdown &amp; Turnaround</b><span>Fast execution with minimal downtime.</span></div>
      <div class="m-item"><span class="icon"></span><b>Mechanical &amp; Electrical Installation</b><span>Industrial-grade installation services.</span></div>
      <div class="m-item"><span class="icon"></span><b>Plant Maintenance</b><span>Preventive and corrective maintenance.</span></div>
      <div class="m-item"><span class="icon"></span><b>Scaffolding &amp; Rope Access</b><span>Safe access for complex structures.</span></div>
      <div class="m-item"><span class="icon"></span><b>Environmental Engineering</b><span>Waste treatment and remediation.</span></div>
      <div class="center"><span class="btn" style="font-size:1.2px;padding:1px 3px">View All Services</span></div>
    </div>
    <div class="light m-sec" style="height:247px">
      <div class="m-eye">PORTFOLIO</div>
      <div class="m-h" style="margin-bottom:4px">Featured Projects</div>
      <div class="m-card proj"><div class="ph" role="img" aria-label="Refinery"></div><div class="cap">Refinery Upgrading Project</div><div class="sub">Oil &amp; Gas</div></div>
      <div class="m-card proj"><div class="ph sky" role="img" aria-label="Power plant"></div><div class="cap">Power Plant Maintenance</div><div class="sub">Power Generation</div></div>
      <div class="m-card proj"><div class="ph blue" role="img" aria-label="Desalination plant"></div><div class="cap">Desalination Plant Project</div><div class="sub">Water Treatment</div></div>
      <div class="m-card proj"><div class="ph green" role="img" aria-label="Waste-to-energy facility"></div><div class="cap">Waste-To-Energy Facility</div><div class="sub">Environmental Solutions</div></div>
    </div>
    <div class="navy center" style="height:43px;padding:5px 3px"><div style="font-size:1.8px;font-weight:700">READY TO BUILD THE FUTURE TOGETHER?</div><div style="font-size:1.2px;margin:2px 0 4px">Our team is ready to deliver world-class solutions for your facility.</div><span class="btn" style="font-size:1.2px;padding:1px 4px">Start Your Project</span> <span style="font-size:1.2px">Contact Team</span></div>
    <div class="center" style="height:60px;padding-top:5px;font-size:1.4px;color:var(--muted);line-height:1.4">
      <div class="m-eye">HOW WE WORK</div><div class="m-h">Our Process</div>
      <div style="display:grid;grid-template-columns:1fr 1fr;gap:6px 2px;margin-top:6px;padding:0 3px"><span>❶ Consultation</span><span>❷ Engineering</span><span>❸ Planning</span><span>❹ Construction</span><span>❺ Testing</span><span>❻ Maintenance</span></div>
    </div>
    <div class="navy" style="height:55px;position:relative;padding:4px 3px;font-size:1.3px;line-height:1.5">
      <div class="ph dusk" role="img" aria-label="Engineers on site" style="position:absolute;right:0;top:0;width:32px;height:100%"></div>
      <div style="position:relative;width:36px"><b style="font-size:1.7px">SAFETY &amp; QUALITY</b><br>Safety is our highest priority.<br><span style="font-size:1.6px">Certifications</span><br>• ISO Certified<br>• PCAB Licensed<br>• HSE Compliant<br><span class="btn" style="font-size:1.1px;padding:.5px 2px">Learn More</span></div>
    </div>
    <div class="light" style="height:92px;padding:5px 3px">
      <div style="font-size:1.8px;font-weight:700;color:var(--navy)">GET IN TOUCH</div>
      <div style="font-size:1.2px;color:var(--muted);margin-top:1px">Don't hesitate to reach out today. We'll be in touch shortly.</div>
      <div class="m-lbl">Name</div><div class="m-field"></div>
      <div class="m-lbl">Email</div><div class="m-field"></div>
      <div class="m-lbl">Subject</div><div class="m-field"></div>
      <div class="m-lbl">Phone</div><div class="m-field"></div>
      <div class="m-lbl">Message</div><div class="m-field" style="height:12px"></div>
      <div class="btn center" style="display:block;font-size:1.2px;margin-top:4px;padding:.5px">Submit</div>
    </div>
    <div style="height:173px;background:var(--navy-dark);color:#dfe3ee;padding:6px 3px;font-size:1.4px;line-height:2.4">
      <div class="brand" style="font-size:2px;justify-content:center"><span class="dot" style="width:4px;height:4px"></span>MIRVANTO</div>
      Mirvanto delivers industrial construction with safety and quality.<br><span style="color:var(--orange)">QUICK LINKS</span><br>About Us · Projects · Careers · Contact<br><span style="color:var(--orange)">INDUSTRIES</span><br>Oil &amp; Gas · Power · Water<br><span style="color:var(--orange)">SERVICES</span><br>Maintenance · Turnaround · Scaffolding<br><span style="color:var(--orange)">GET IN TOUCH</span><br>Tanauan City, Batangas<br>+63 (0) 45 210-3377<br>info@mirvanto.ph<br>Copyright © 2026 MIRVANTO
    </div>
  </div>

</div>
</body>
</html>
```